Marisol business card and stationary
business card and stationary
Marisol business card and stationary - Retailers
Creative Brief
Bright & Fun-filled
Janet Wroblenko
owner, designer
marisol a florist 418 north brook lane greenville, sc 29174
info@marisolblooms.example
marisolblooms.example
Concepts
Stationery for Online Retailer

```html
<!DOCTYPE html>
<html lang="en">
<head>
<meta charset="utf-8">
<title>Marisol – Business Card</title>
<link href="https://fonts.googleapis.com/css2?family=Questrial&family=Dancing+Script:wght@700&display=swap" rel="stylesheet">
<style>
  :root {
    --backdrop: #efe9e1;
    --card-green: #9db23c;
    --card-green-light: #adc24a;
    --ink-dark: #3f4a16;
    --ink-white: #ffffff;
    --petal-pink: #f2a7b4;
    --divider: rgba(255,255,255,0.55);
  }
  html, body {
    margin: 0;
    padding: 0;
    width: 1200px;
    height: 811px;
    overflow: hidden;
    background: var(--backdrop);
  }
  .canvas {
    position: relative;
    width: 1200px;
    height: 811px;
    font-family: "Questrial", "Helvetica Neue", Arial, sans-serif;
  }
  .card {
    position: absolute;
    top: 255px;
    width: 520px;
    height: 300px;
    background: linear-gradient(160deg, var(--card-green-light), var(--card-green));
    border-radius: 14px 70px 14px 70px;
    box-shadow: 0 10px 24px rgba(60,50,30,0.22);
    overflow: hidden;
  }
  .card--front { left: 55px; }
  .card--back { left: 625px; }

  .brand {
    position: absolute;
    display: flex;
    align-items: center;
    gap: 14px;
  }
  .brand__mark {
    width: 64px;
    height: 64px;
    border-radius: 50%;
    background: var(--petal-pink);
  }
  .brand__name {
    font-size: 40px;
    color: var(--ink-dark);
    letter-spacing: 0.5px;
  }
  .card--front .brand { left: 34px; top: 76px; }
  .card--back .brand { left: 180px; top: 110px; }
  .card--back .brand__mark { width: 84px; height: 84px; }
  .card--back .brand__name { font-size: 48px; }

  .divider {
    position: absolute;
    left: 262px;
    top: 60px;
    width: 1px;
    height: 130px;
    background: var(--divider);
  }
  .website {
    position: absolute;
    right: 56px;
    top: 30px;
    font-size: 13px;
    color: var(--ink-white);
  }
  .person {
    position: absolute;
    left: 290px;
    top: 110px;
    color: var(--ink-white);
  }
  .person__name {
    font-family: "Dancing Script", "Brush Script MT", cursive;
    font-size: 24px;
    line-height: 1.1;
  }
  .person__role {
    font-size: 12px;
    padding-left: 14px;
  }
  .contact {
    position: absolute;
    left: 34px;
    bottom: 30px;
    font-size: 13px;
    line-height: 1.55;
    color: var(--ink-dark);
  }
</style>
</head>
<body>
<main class="canvas">

  <section class="card card--front" aria-label="Business card front">
    <div class="brand">
      <span class="brand__mark"></span>
      <span class="brand__name">marisol</span>
    </div>
    <div class="divider"></div>
    <div class="website">www.marisolblooms.example</div>
    <div class="person">
      <div class="person__name">Janet Wroblenko</div>
      <div class="person__role">owner, designer</div>
    </div>
    <div class="contact">
      <div>info@marisolblooms.example &nbsp;Ph: 864 555 0147</div>
      <div>marisol a florist, 418 north brook lane greenville, sc 29174</div>
    </div>
  </section>

  <section class="card card--back" aria-label="Business card back">
    <div class="brand">
      <span class="brand__mark"></span>
      <span class="brand__name">marisol</span>
    </div>
  </section>

</main>
</body>
</html>
```